New Business Card Design Project

We are looking for a talented individual to create a truly awesome/unique business card design for us. We are looking for a someone to design something that will really stand out from the crowd - we don't mind what ideas you come up with (ie embossed/flat/matte/shine etc etc) just wow us with your creativity.
Updates

Target Market(s)

Video Games Industry Professionals (all levels of seniority from QA Testers through to CEOs)

Contact Information for Business Card

Company logo (see upload)
Company name: Northbay Play Careers Ltd
Employee Name: Darren Elsby
Job title: CEO
Website: www.nbpc2go.example
Office +44 1632 960418
Mobile: +44 7700 900276
Email: darren@nbpc2go.example

Colors

Designer to choose colors to be used in the design.

Requirements
Must have
• The business card design MUST contain all the information listed in the BUSINESS CARD DETAILS box.
• You will see the colours that are relevant to us (ie company logo) in the uploaded imagery - however you do not have to use all these colours when designing the business card itself
• MUST BE DOUBLE SIDED

```html
<!DOCTYPE html>
<html lang="en">
<head>
<meta charset="utf-8">
<title>Northbay Play Careers – Business Card</title>
<link rel="stylesheet" href="https://fonts.googleapis.com/css2?family=Mulish:wght@400;600;800&display=swap">
<style>
  :root {
    --backdrop: #fbf3d2;
    --orange: #ff6000;
    --navy: #0c1a80;
    --sun: #f2e23a;
    --white: #ffffff;
    --ink: #111111;
    --card-shadow: 0 6px 18px rgba(0, 0, 0, 0.18);
  }
  html, body {
    margin: 0;
    padding: 0;
    width: 1200px;
    height: 1200px;
    overflow: hidden;
    background: var(--backdrop);
    font-family: "Mulish", Arial, sans-serif;
  }
  .canvas {
    position: relative;
    width: 1200px;
    height: 1200px;
  }
  .card {
    position: absolute;
    left: 162px;
    width: 876px;
    height: 500px;
    box-shadow: var(--card-shadow);
    overflow: hidden;
  }
  /* Front side */
  .card-front {
    top: 80px;
    background: var(--orange);
  }
  .mascot-art {
    position: absolute;
    left: 0;
    top: 0;
    width: 420px;
    height: 500px;
    background:
      radial-gradient(circle at 42% 82%, var(--sun) 0 26%, transparent 26.5%),
      radial-gradient(ellipse at 45% 45%, var(--navy) 0 38%, rgba(12, 26, 128, 0.55) 52%, transparent 70%);
  }
  .front-brand {
    position: absolute;
    left: 440px;
    top: 168px;
    width: 400px;
    text-align: center;
  }
  .front-brand .company-name {
    margin: 0;
    color: var(--white);
    font-weight: 800;
    font-size: 50px;
    line-height: 1.1;
    letter-spacing: 0.5px;
  }
  .front-brand .website {
    margin: 30px 0 0;
    color: var(--white);
    font-weight: 400;
    font-size: 19px;
    letter-spacing: 0.5px;
  }
  /* Back side */
  .card-back {
    top: 640px;
    background: var(--white);
  }
  .back-brand {
    position: absolute;
    left: 40px;
    top: 52px;
    margin: 0;
    color: var(--navy);
    font-weight: 800;
    font-size: 40px;
    line-height: 1.1;
    width: 360px;
  }
  .person {
    position: absolute;
    left: 40px;
    top: 190px;
  }
  .person .name {
    margin: 0;
    color: var(--navy);
    font-weight: 800;
    font-size: 32px;
  }
  .person .role {
    margin: 10px 0 0;
    color: var(--ink);
    font-weight: 800;
    font-size: 18px;
  }
  .contacts {
    position: absolute;
    left: 34px;
    top: 322px;
    list-style: none;
    margin: 0;
    padding: 0;
  }
  .contacts li {
    display: flex;
    align-items: center;
    height: 46px;
    font-size: 21px;
    color: var(--ink);
    letter-spacing: 0.3px;
  }
  .contacts svg {
    width: 34px;
    height: 34px;
    margin-right: 12px;
    flex: none;
  }
  .hair-art {
    position: absolute;
    right: 0;
    top: 40px;
    width: 320px;
    height: 400px;
    background: radial-gradient(ellipse at 100% 50%, var(--navy) 0 40%, rgba(12, 26, 128, 0.45) 60%, transparent 78%);
  }
</style>
</head>
<body>
<main class="canvas">

  <section class="card card-front" aria-label="Card front">
    <div class="mascot-art" role="img" aria-label="Mascot illustration: a bearded warrior in a horned helmet with flowing hair, before a striped yellow sun"></div>
    <div class="front-brand">
      <p class="company-name">Northbay Play Careers</p>
      <p class="website">www.nbpc2go.example</p>
    </div>
  </section>

  <section class="card card-back" aria-label="Card back">
    <p class="back-brand">Northbay Play Careers</p>

    <div class="person">
      <p class="name">Darren Elsby</p>
      <p class="role">CEO</p>
    </div>

    <ul class="contacts">
      <li>
        <svg viewBox="0 0 24 24" aria-hidden="true"><path fill="#111" d="M6.6 10.8a15.1 15.1 0 0 0 6.6 6.6l2.2-2.2c.3-.3.7-.4 1-.2 1.1.4 2.3.6 3.6.6.6 0 1 .4 1 1V20c0 .6-.4 1-1 1C10.6 21 3 13.4 3 4c0-.6.4-1 1-1h3.5c.6 0 1 .4 1 1 0 1.3.2 2.5.6 3.6.1.3 0 .7-.2 1z"/></svg>
        +44 1632 960418
      </li>
      <li>
        <svg viewBox="0 0 24 24" aria-hidden="true"><rect x="6.5" y="1.5" width="11" height="21" rx="2" fill="none" stroke="#111" stroke-width="1.6"/><line x1="7" y1="18.5" x2="17" y2="18.5" stroke="#111" stroke-width="1.2"/><line x1="7" y1="4.5" x2="17" y2="4.5" stroke="#111" stroke-width="1.2"/></svg>
        +44 7700 900276
      </li>
      <li>
        <svg viewBox="0 0 24 24" aria-hidden="true"><rect x="1.5" y="5" width="21" height="14" fill="#111"/><polyline points="1.5,5 12,13 22.5,5" fill="none" stroke="#fff" stroke-width="1.4"/></svg>
        darren@nbpc2go.example
      </li>
    </ul>

    <div class="hair-art" role="img" aria-label="Decorative flowing navy hair strands from the mascot illustration"></div>
  </section>

</main>
</body>
</html>
```